Tallwood Ridge firewood

It a new firewood outlet in Jindabyne nsw that will only sell top hardwood firewood (ironbark , red gum, grey gum, an box mix. I would like to see a web page the we can do order online payment for delivery. It will all so need to have photos of the firewood. I all so have logo for tallwood ridge firewood
Must have a modem look but easy to use I would like to see a black back ground of some sort.

Here are some other firewood web pages for ideas and firewood info
http://www.kestrelburnfuel.com.au
http://www.brindlefirewood.com.au
http://www.coppertonfirewood.com.au
http://www.wattleyhearthlogs.com.au/firewood

```html
<!DOCTYPE html>
<html lang="en">
<head>
<meta charset="utf-8">
<title>Tallwood Ridge Firewood</title>
<link href="https://fonts.googleapis.com/css2?family=Oswald:wght@400;500;700&family=Open+Sans:wght@400;600;700&display=swap" rel="stylesheet">
<style>
:root{
  --ink:#111111;
  --black:#0a0a0a;
  --blue:#1d64b5;
  --blue-dark:#154e90;
  --orange:#f39a1e;
  --gold:#f6c343;
  --tan:#b88a5c;
  --tan-light:#d6b48c;
  --paper:#ffffff;
  --grey:#f1f1f1;
  --text:#444444;
  --muted:#9a9a9a;
}
*{box-sizing:border-box;margin:0;padding:0}
html,body{width:828px;height:1200px;overflow:hidden;background:var(--paper);font-family:"Open Sans",sans-serif;color:var(--text)}
.page{position:relative;width:828px;height:1200px}

.topbar{position:absolute;top:0;left:0;width:828px;height:26px;background:var(--black);display:flex;align-items:center;justify-content:space-between;padding:0 40px;font-size:9px;color:#ddd;font-weight:600}
.social{display:flex;align-items:center;gap:5px}
.social .dot{width:13px;height:13px;border-radius:50%;background:var(--blue)}
.callus{display:flex;align-items:center;gap:6px}
.callus b{font-family:"Oswald",sans-serif;font-size:14px;color:#fff;font-weight:500}

.nav{position:absolute;top:26px;left:0;width:828px;height:38px;background:var(--blue);display:flex;align-items:center;font-family:"Oswald",sans-serif;font-size:12px;color:#fff;letter-spacing:.5px}
.nav a{color:#fff;text-decoration:none;padding:0 16px;height:38px;line-height:38px}
.nav a.active{background:var(--orange)}
.nav .left{position:absolute;left:40px;display:flex}
.nav .right{position:absolute;right:40px;display:flex}

.brand{position:absolute;top:2px;left:344px;width:140px;height:96px;background:var(--paper);border-radius:0 0 10px 10px;display:flex;flex-direction:column;align-items:center;justify-content:center;gap:6px;z-index:3;box-shadow:0 2px 6px rgba(0,0,0,.35)}
.brand .mark{width:34px;height:34px;border-radius:50%;background:var(--blue)}
.brand .name{font-family:"Oswald",sans-serif;font-weight:700;font-size:13px;color:var(--blue);text-align:center;line-height:1.1;text-transform:uppercase}

.hero{position:absolute;top:64px;left:0;width:828px;height:324px;background:linear-gradient(135deg,#5a3b22 0%,#3a2615 45%,#6b4a2c 75%,#2a1b0e 100%)}
.hero .woodsman{position:absolute;left:500px;top:18px;width:210px;height:306px;background:linear-gradient(180deg,#2f6fb5 0%,#22528a 60%,#1b3f6a 100%);border-radius:90px 90px 0 0;opacity:.9}
.hero h1{position:absolute;left:48px;top:92px;font-family:"Oswald",sans-serif;font-weight:700;font-size:42px;line-height:1;color:#fff;text-transform:uppercase;text-shadow:0 2px 4px rgba(0,0,0,.6)}
.hero h1 span{display:block;color:var(--orange);font-size:48px}
.hero .tagline{position:absolute;left:48px;top:200px;font-family:"Oswald",sans-serif;font-size:19px;line-height:1.25;color:var(--gold);text-shadow:0 1px 3px rgba(0,0,0,.6)}
.hero .arrow{position:absolute;top:140px;width:22px;height:40px;background:rgba(0,0,0,.55);display:flex;align-items:center;justify-content:center}
.hero .arrow.prev{left:0}
.hero .arrow.next{right:0}
.order-tab{position:absolute;left:592px;top:344px;width:196px;height:44px;background:var(--orange);color:#fff;font-family:"Oswald",sans-serif;font-size:18px;font-weight:500;display:flex;align-items:center;justify-content:center;text-transform:uppercase;letter-spacing:.5px}

.welcome{position:absolute;top:388px;left:0;width:828px;height:277px;background:var(--paper)}
.welcome h2{position:absolute;left:40px;top:22px;font-family:"Oswald",sans-serif;font-weight:700;font-size:19px;color:var(--ink);text-transform:uppercase}
.welcome h2 em{font-style:normal;color:var(--blue)}
.welcome .rule{position:absolute;left:40px;top:52px;width:520px;height:1px;background:#ddd}
.video{position:absolute;left:40px;top:66px;width:150px;height:92px;background:linear-gradient(135deg,#e06a1a,#7a2d0c 70%,#2b1206);display:flex;align-items:center;justify-content:center}
.intro{position:absolute;left:204px;top:66px;width:356px;font-size:9px;line-height:1.45}
.intro strong{color:var(--ink);font-size:10px}
.body-copy{position:absolute;left:40px;top:166px;width:520px;font-size:9px;line-height:1.5}

.order-form{position:absolute;left:592px;top:0;width:196px;height:268px;background:var(--tan);padding:10px 14px}
.order-form p{font-size:7.5px;line-height:1.35;color:#fff;margin-bottom:8px}
.field{height:15px;background:#fff;margin-bottom:4px;font-size:7px;color:var(--muted);padding:3px 5px}
.next-btn{margin-top:8px;width:100%;height:28px;background:var(--blue);color:#fff;font-family:"Oswald",sans-serif;font-size:17px;font-weight:700;display:flex;align-items:center;justify-content:center;gap:6px}

.products{position:absolute;top:665px;left:0;width:828px;height:220px;background:var(--grey)}
.products h2{position:absolute;top:22px;width:828px;text-align:center;font-family:"Oswald",sans-serif;font-weight:700;font-size:22px;color:var(--blue);text-transform:uppercase}
.products h2 span{color:var(--orange)}
.product-row{position:absolute;top:66px;left:78px;display:flex;gap:20px}
.product{width:153px;text-align:center}
.product .photo{height:90px;background:linear-gradient(135deg,#8a5a32,#5b3a1d 60%,#a57a4c);margin-bottom:8px}
.product .photo.light{background:linear-gradient(135deg,#c9a176,#8e6640 60%,#d5b38a)}
.product .photo.kindling{background:linear-gradient(135deg,#b8875a,#6e4624 60%,#c79a6a)}
.product .photo.mulch{background:linear-gradient(135deg,#7a5532,#4e331b 60%,#94693f)}
.product h3{font-family:"Oswald",sans-serif;font-size:11px;font-weight:500;color:var(--ink);text-transform:uppercase}
.product .price{font-family:"Oswald",sans-serif;font-size:12px;color:var(--orange);font-weight:700}
.product .price small{font-size:8px;color:var(--muted);font-weight:400}
.products .arrow{position:absolute;top:98px;width:22px;height:22px;border-radius:50%;background:#999;display:flex;align-items:center;justify-content:center}
.products .arrow.prev{left:42px}
.products .arrow.next{right:42px}

.footer{position:absolute;top:885px;left:0;width:828px;height:280px;background:var(--ink);color:#bbb;padding:38px 40px 0}
.footer .cols{display:flex;gap:40px}
.footer h4{font-family:"Oswald",sans-serif;font-size:13px;color:var(--orange);text-transform:uppercase;margin-bottom:10px;font-weight:500}
.footer ul{list-style:none;font-size:9px;line-height:1.8;text-transform:uppercase}
.footer .links{display:flex;gap:40px;width:240px}
.hotline{width:230px}
.hotline .num{font-family:"Oswald",sans-serif;font-size:17px;color:#fff;line-height:1.3}
.hotline p{font-size:7.5px;line-height:1.5;margin-top:8px}
.hours ul{line-height:1.9}
.copyright{position:absolute;top:1165px;left:0;width:828px;height:35px;background:#000;color:#777;font-size:8px;display:flex;align-items:center;justify-content:center}
</style>
</head>
<body>
<div class="page">

  <div class="topbar">
    <div class="social">FOLLOW US ON <span class="dot"></span><span class="dot"></span><span class="dot"></span><span class="dot"></span><span class="dot"></span></div>
    <div class="callus">CALL US NOW
      <svg width="12" height="12" viewBox="0 0 24 24"><path fill="#f39a1e" d="M6.6 10.8a15 15 0 0 0 6.6 6.6l2.2-2.2a1 1 0 0 1 1-.25 11.4 11.4 0 0 0 3.6.57 1 1 0 0 1 1 1V20a1 1 0 0 1-1 1A17 17 0 0 1 3 4a1 1 0 0 1 1-1h3.5a1 1 0 0 1 1 1 11.4 11.4 0 0 0 .57 3.6 1 1 0 0 1-.25 1z"/></svg>
      <b>0400 555 218</b></div>
  </div>

  <nav class="nav">
    <div class="left"><a class="active">HOME</a><a>ABOUT US</a><a>ORDER ONLINE</a></div>
    <div class="right"><a>FAQ</a><a>OUR PRODUCTS</a><a>CONTACT US</a></div>
  </nav>

  <div class="brand"><span class="mark"></span><span class="name">Tallwood Ridge<br>Firewood</span></div>

  <section class="hero">
    <div class="woodsman" role="img" aria-label="Illustration of a woodsman holding an axe"></div>
    <h1>Tallwood Ridge<span>Firewood</span></h1>
    <p class="tagline">Wood That Gets You Hot And<br>Last All Night Long</p>
    <div class="arrow prev"><svg width="10" height="14" viewBox="0 0 10 14"><path d="M8 1 2 7l6 6" stroke="#fff" stroke-width="2" fill="none"/></svg></div>
    <div class="arrow next"><svg width="10" height="14" viewBox="0 0 10 14"><path d="m2 1 6 6-6 6" stroke="#fff" stroke-width="2" fill="none"/></svg></div>
    <div class="order-tab">Order Firewood</div>
  </section>

  <section class="welcome">
    <h2>Welcome <em>to our new online store</em></h2>
    <div class="rule"></div>
    <div class="video" role="img" aria-label="Video still of a log fire burning">
      <svg width="34" height="34" viewBox="0 0 34 34"><circle cx="17" cy="17" r="16" fill="rgba(0,0,0,.5)"/><path d="M13 10v14l11-7z" fill="#fff"/></svg>
    </div>
    <p class="intro"><strong>Top quality hardwood firewood delivered to your door in Jindabyne and the surrounding region.</strong> We stock only seasoned ironbark, red gum, grey gum and box mix, split to size and ready to burn. Choose your load, pick a delivery day and pay securely online in a few easy steps. Our wood burns hot, slow and clean all winter long.</p>
    <p class="body-copy">Every load is cut from sustainable sources and dried for at least twelve months, so you get less smoke and more heat from every log. Order a single trailer or a full truck, add kindling to get started, and we will stack it where you need it. Need advice on the right mix for your heater? Give our friendly team a call any day of the week.</p>

    <form class="order-form">
      <p>Place your order online today and we will deliver seasoned hardwood straight to your home. Fill in your details below to get started.</p>
      <div class="field">Name</div>
      <div class="field">Email</div>
      <div class="field">Phone</div>
      <div class="field">Address</div>
      <div class="field">Suburb</div>
      <div class="field">Wood Type</div>
      <div class="field">Quantity</div>
      <div class="field">Delivery Date</div>
      <div class="next-btn">NEXT
        <svg width="14" height="14" viewBox="0 0 14 14"><circle cx="7" cy="7" r="7" fill="#fff"/><path d="m5.5 3.5 3.5 3.5-3.5 3.5" stroke="#1d64b5" stroke-width="2" fill="none"/></svg>
      </div>
    </form>
  </section>

  <section class="products">
    <h2>New products for <span>February</span></h2>
    <div class="arrow prev"><svg width="8" height="10" viewBox="0 0 8 10"><path d="M6 1 2 5l4 4" stroke="#fff" stroke-width="2" fill="none"/></svg></div>
    <div class="product-row">
      <div class="product"><div class="photo" role="img" aria-label="Photo of mixed hardwood logs"></div><h3>Mixed Hardwood</h3><div class="price">$25.00 <small>/ bag</small></div></div>
      <div class="product"><div class="photo light" role="img" aria-label="Photo of unsplit wood rounds"></div><h3>Unsplit Wood</h3><div class="price">$100 <small>/ load</small></div></div>
      <div class="product"><div class="photo kindling" role="img" aria-label="Photo of a bundle of kindling"></div><h3>Bunch of Kindling</h3><div class="price">$8.00 <small>/ bunch</small></div></div>
      <div class="product"><div class="photo mulch" role="img" aria-label="Photo of plain wood mulch"></div><h3>Plain Wood Mulch</h3><div class="price">$25.00 <small>/ m³</small></div></div>
    </div>
    <div class="arrow next"><svg width="8" height="10" viewBox="0 0 8 10"><path d="m2 1 4 4-4 4" stroke="#fff" stroke-width="2" fill="none"/></svg></div>
  </section>

  <footer class="footer">
    <div class="cols">
      <div>
        <h4>Navigation</h4>
        <div class="links">
          <ul><li>Home</li><li>About Us</li><li>Our Products</li><li>Firewood</li><li>Fencing</li></ul>
          <ul><li>Fencing</li><li>Contact</li><li>Conditions of Use</li><li>Privacy Policy</li></ul>
        </div>
      </div>
      <div class="hotline">
        <h4>Enquiry Hotline</h4>
        <div class="num">0355 501 274</div>
        <div class="num">0400 555 219</div>
        <p>Call us seven days for orders, delivery times and advice on the best hardwood for your fire.</p>
      </div>
      <div class="hours">
        <h4>Hours</h4>
        <ul><li>Mon-Thur 8:00am-5:00pm</li><li>Friday 8:00am-6:00pm</li><li>Saturday 8:00am-5:00pm</li><li>Sunday 9:00am-3:00pm</li></ul>
      </div>
    </div>
  </footer>
  <div class="copyright">Copyright © 2015 Tallwood Ridge Firewood. All Rights Reserved.</div>

</div>
</body>
</html>
```